Digital Marketing Website Design

I need the homepage designed for my new digital marketing agency I am starting. The main goal for this homepage is to drive people to make an appointment for me to discuss their upcoming projects. Here are some examples of the layouts that I would like to emulate.
https://www.tallmarsh.com/
https://www.quillforge.com/
https://pebblenook.com/
https://drvenholt.com/
https://www.quietlyrooted.org/
My main focus is to attract leads that need help with running digital ads such as Chatterly ads and Finder Promos. I do offer other services like SEO and other things but the main focus is digital Ads.
The final design should communicate Orchid Digital is a Digital marketing strategist building predictable revenue for small businesses through digital ads, email and marketing automation.
Target Market(s)
30-55, business owners, income 100K+, ecommerce companies, etc.
Industry/Entity Type
Digital Marketing
Number of Pages Required
2 page
Font styles to use
Requirements
Must have
- An appealing look and feel set to drive people to make an appointment.
Logo
There needs to be a call to action button in the far right of the navigation
The same call to action in the navigation needs to be in each section on the homepage.
I need the homepage and an about us page.

```html
<!DOCTYPE html>
<html lang="en">
<head>
<meta charset="utf-8">
<title>Orchid Digital — Predictable Revenue for Small Businesses</title>
<link rel="stylesheet" href="https://fonts.googleapis.com/css2?family=Lato:ital,wght@0,400;0,700;0,900;1,700&family=Open+Sans:wght@700&display=swap">
<style>
:root{
  --orange:#f26a2e;
  --orange-deep:#e8452f;
  --red-top:#e63a3f;
  --red-bottom:#f3706d;
  --ink:#2b2b2b;
  --ink-soft:#555;
  --nav:#3b4a5a;
  --footer:#232323;
  --footer-text:#e4e4e4;
  --white:#fff;
  --line:#dcdcdc;
}
*{margin:0;padding:0;box-sizing:border-box}
html,body{width:1200px;height:3130px;overflow:hidden}
body{position:relative;background:var(--white);font-family:'Lato',sans-serif;color:var(--ink)}
.abs{position:absolute}

/* header */
.site-header{left:0;top:0;width:1200px;height:119px;background:var(--white)}
.brand{left:75px;top:50px;display:flex;align-items:center;gap:8px;font-weight:900;font-size:27px;letter-spacing:-0.5px;color:var(--ink);text-transform:uppercase;line-height:1}
.brand-dot{width:16px;height:16px;border-radius:50%;background:var(--orange)}
.main-nav a{position:absolute;top:54px;font-size:15px;font-weight:700;color:var(--nav);text-decoration:none;text-transform:uppercase}
.btn-cta{display:flex;align-items:center;justify-content:center;background:linear-gradient(90deg,var(--orange-deep),var(--orange));color:var(--white);font-weight:900;text-transform:uppercase;text-decoration:none;font-size:17px}
.nav-cta{left:857px;top:34px;width:271px;height:55px}

/* hero */
.hero{left:0;top:119px;width:1200px;height:789px}
.hero-title{left:0;top:316px;width:1200px;text-align:center;font-family:'Open Sans',sans-serif;font-weight:700;font-size:53px;line-height:57px;color:var(--white)}
.hero-sub{left:0;top:444px;width:1200px;text-align:center;font-family:'Open Sans',sans-serif;font-weight:700;font-size:28px;line-height:38px;color:var(--white)}
.btn-outline{left:353px;top:558px;width:290px;height:54px;border:2px solid var(--white);display:flex;align-items:center;justify-content:center;color:var(--white);font-weight:900;font-size:15px;text-transform:uppercase;text-decoration:none}
.hero-read{left:668px;top:558px;width:179px;height:54px}
.slider-dots{left:558px;top:737px;display:flex;gap:12px}
.slider-dots span{width:12px;height:12px;border-radius:50%;background:var(--white)}
.slider-dots span.active{background:var(--orange)}

/* clients */
.client{top:984px;width:193px;height:90px;border:1px solid var(--line);background:#fcfcfc;box-shadow:0 1px 3px rgba(0,0,0,.08);display:flex;align-items:center;justify-content:center;gap:10px;font-weight:700;font-size:28px;color:#333}
.client i{width:28px;height:28px;border-radius:50%;background:var(--orange)}
.client i.blue{background:#2d8ed8}

/* how it works */
.how-bg{left:0;top:1151px}
.section-title{left:0;width:1200px;text-align:center;font-weight:900;color:var(--white);text-transform:uppercase}
.how-title{top:1259px;font-size:34px}
.how-copy{left:88px;width:1024px;text-align:center;color:var(--white);font-size:17px;line-height:32px}
.how-sub{top:1560px;font-size:23px}
.step-circle{width:80px;height:80px;border-radius:50%;background:var(--white);display:flex;align-items:center;justify-content:center}
.step-circle.active{border:4px solid var(--ink);box-shadow:inset 0 0 0 4px var(--orange)}
.step-name{width:320px;text-align:center;color:var(--white);font-weight:700;font-size:22px}
.step-text{width:320px;text-align:center;color:var(--white);font-size:15px;line-height:24px}

/* testimonials */
.testi-title{left:75px;top:2214px;font-weight:900;font-size:34px;color:#3a3a3a;text-transform:uppercase}
.quote-mark{left:75px;top:2296px}
.testi-text{left:75px;top:2340px;width:520px;font-size:17.5px;line-height:31.5px;color:var(--ink-soft)}
.testi-name{left:75px;top:2512px;font-weight:900;font-size:25px;color:var(--orange);text-transform:uppercase}
.testi-company{left:75px;top:2548px;font-weight:700;font-style:italic;font-size:15px;color:var(--orange-deep)}
.testi-dots{left:75px;top:2614px;display:flex;gap:8px}
.testi-dots span{width:10px;height:10px;border-radius:50%;background:#777}
.testi-dots span.active{background:var(--orange)}
.portraits{left:660px;top:2220px}

/* footer */
.footer-bg{left:0;top:2729px}
.footer-brand{left:75px;top:2932px;display:flex;align-items:center;gap:8px;font-weight:900;font-size:25px;color:var(--white);text-transform:uppercase;line-height:1}
.footer-small{left:75px;font-size:12.5px;line-height:23px;color:var(--footer-text)}
.footer-col h4{font-size:15px;font-weight:900;color:var(--orange);text-transform:uppercase;margin-bottom:8px}
.footer-col li{list-style:none;font-size:14.5px;line-height:30.4px;color:var(--footer-text)}
.contact-row{left:864px;display:flex;gap:22px;font-size:14px;line-height:22px;color:var(--footer-text)}
.contact-row svg{flex:none;margin-top:4px}
.social{left:864px;top:3042px;display:flex;gap:14px}
.social span{font-size:13px;font-weight:700;color:var(--white)}
</style>
</head>
<body>

<header class="abs site-header">
  <div class="abs brand"><span class="brand-dot"></span>Orchid Digital</div>
  <nav class="main-nav">
    <a style="left:524px" href="#about">About</a>
    <a style="left:610px" href="#how">How it Works</a>
    <a style="left:757px" href="#contact">Contact</a>
  </nav>
  <a class="abs btn-cta nav-cta" href="#schedule">Schedule Appointment</a>
</header>

<section class="abs hero" id="about">
  <svg class="abs" style="left:0;top:0" width="1200" height="789" role="img" aria-label="Photo of a team working together in a bright, creative open-plan office">
    <defs>
      <linearGradient id="heroFill" x1="0" y1="0" x2="1" y2="1">
        <stop offset="0" stop-color="#6d6a66"/>
        <stop offset=".5" stop-color="#5a5c5f"/>
        <stop offset="1" stop-color="#3f4245"/>
      </linearGradient>
    </defs>
    <polygon points="0,0 1200,0 1200,789 600,683 0,789" fill="url(#heroFill)"/>
  </svg>
  <h1 class="abs hero-title" style="top:197px">We Built Profitable Ad Campaigns<br>For Small Businesses</h1>
  <p class="abs hero-sub" style="top:323px">The selling system that brings in Predictable revenue through<br>digital ads, email, and marketing automation.</p>
  <a class="abs btn-outline" style="top:439px" href="#checklist">Free Chatterly Ads Checklist</a>
  <a class="abs btn-cta hero-read" style="top:439px" href="#how">Read More</a>
  <div class="abs slider-dots" style="top:618px"><span class="active"></span><span></span><span></span><span></span></div>
</section>

<section class="clients">
  <div class="abs client" style="left:75px"><i></i>Brightwell</div>
  <div class="abs client" style="left:290px"><i></i>Marlow</div>
  <div class="abs client" style="left:505px"><i class="blue"></i>Steadfast</div>
  <div class="abs client" style="left:719px"><i></i>Keystone</div>
  <div class="abs client" style="left:934px"><i class="blue"></i>Tasko</div>
</section>

<section id="how">
  <svg class="abs how-bg" width="1200" height="984" role="img" aria-label="Red-tinted photo of a team planning around a table">
    <defs>
      <linearGradient id="howFill" x1="0" y1="0" x2="0" y2="1">
        <stop offset="0" stop-color="var(--red-top)"/>
        <stop offset="1" stop-color="var(--red-bottom)"/>
      </linearGradient>
    </defs>
    <polygon points="0,107 600,0 1200,107 1200,984 600,897 0,984" fill="url(#howFill)"/>
  </svg>
  <h2 class="abs section-title how-title">How it Works</h2>
  <p class="abs how-copy" style="top:1318px">At Orchid Digital Solutions we know that you want to have a profitable business. In order to do that, you need a strong system that can predictably bring in sales even in bad times. The problem is there is so much out there to wade through and so many people telling you what you should do which makes you feel frustrated, lost, and flat out stressed out. We believe that businesses with great products should get the customer.</p>
  <p class="abs how-copy" style="top:1462px;left:200px;width:800px">We understand the frustration which is why we are here to help you maneuver through the minutiae and create a system that flat out works.</p>
  <h3 class="abs section-title how-sub">Here's How We Do It:</h3>

  <svg class="abs" style="left:0;top:1610px" width="1200" height="60">
    <path d="M239 58 V5 H962 V58 M600 5 V58" fill="none" stroke="#fff" stroke-width="3"/>
  </svg>

  <div class="abs step-circle active" style="left:199px;top:1662px">
    <svg width="40" height="40" viewBox="0 0 40 40"><rect x="4" y="7" width="32" height="29" rx="2" fill="var(--orange)"/><rect x="8" y="15" width="24" height="17" fill="#fff"/><g fill="var(--orange)"><rect x="10" y="17" width="5" height="4"/><rect x="17" y="17" width="5" height="4"/><rect x="24" y="17" width="5" height="4"/><rect x="10" y="24" width="5" height="4"/><rect x="17" y="24" width="5" height="4"/><rect x="24" y="24" width="5" height="4"/></g><rect x="11" y="3" width="3" height="8" fill="var(--orange)"/><rect x="26" y="3" width="3" height="8" fill="var(--orange)"/></svg>
  </div>
  <div class="abs step-circle" style="left:560px;top:1662px">
    <svg width="44" height="40" viewBox="0 0 44 40" fill="#555"><circle cx="22" cy="11" r="7"/><path d="M10 32c0-8 5-12 12-12s12 4 12 12z"/><circle cx="9" cy="15" r="5"/><path d="M0 32c0-6 3-9 9-9 2 0 3 .5 4 1-2 2-3 5-3 8z"/><circle cx="35" cy="15" r="5"/><path d="M44 32c0-6-3-9-9-9-2 0-3 .5-4 1 2 2 3 5 3 8z"/></svg>
  </div>
  <div class="abs step-circle" style="left:922px;top:1662px">
    <svg width="42" height="38" viewBox="0 0 42 38" fill="#555"><path d="M2 2h3v31h35v3H2z"/><rect x="10" y="20" width="5" height="11"/><rect x="18" y="12" width="5" height="19"/><rect x="26" y="16" width="5" height="15"/><rect x="34" y="8" width="5" height="23"/></svg>
  </div>

  <p class="abs step-name" style="left:79px;top:1764px">Step 1</p>
  <p class="abs step-name" style="left:440px;top:1764px">Step 2</p>
  <p class="abs step-name" style="left:802px;top:1764px">Step 3</p>
  <p class="abs step-text" style="left:79px;top:1802px">Schedule an appointment to go through the basics of what you need and to find out if we are a good fit to work together.</p>
  <p class="abs step-text" style="left:430px;top:1802px;width:340px">Work with our team to build out your customer journey and selling system</p>
  <p class="abs step-text" style="left:862px;top:1802px;width:200px">Execute and enjoy the extra revenue!</p>

  <p class="abs how-copy" style="top:1915px;left:120px;width:960px">So, schedule your appointment today. And in the meantime, checkout our Chatterly ads checklist. So you can stop any poor running campaigns and fill in the gaps where they are needed.</p>
</section>

<section class="testimonials">
  <h2 class="abs testi-title">What Others Are Saying...</h2>
  <svg class="abs quote-mark" width="36" height="30" viewBox="0 0 36 30" fill="#c9c9c9"><path d="M0 30V16C0 6 5 1 14 0v5c-5 1-7 4-7 9h7v16zM21 30V16c0-10 5-15 14-16v5c-5 1-7 4-7 9h7v16z"/></svg>
  <p class="abs testi-text">Consectetur adipiscing elit ut&nbsp; ultricies lectusonec porttitor, nisl ac pellentesque faucibus, ante ante imperdiet augue, ut sodales sapien metus et mauris. Nullam eget odio dignissim, pharetra lacus in, gravida augueerat volutpat&nbsp; pellentesque, dolor sit amet posuere accumsan, mauris odio blandit massa, porttitor..”</p>
  <p class="abs testi-name">Nell Dorsey</p>
  <p class="abs testi-company">Company Name</p>
  <div class="abs testi-dots"><span class="active"></span><span></span><span></span></div>

  <svg class="abs portraits" width="460" height="450" viewBox="660 2220 460 450">
    <defs>
      <linearGradient id="portraitFill" x1="0" y1="0" x2="0" y2="1">
        <stop offset="0" stop-color="#d9d9d9"/>
        <stop offset="1" stop-color="#8a8e95"/>
      </linearGradient>
    </defs>
    <g role="img" aria-label="Portrait of a client giving a testimonial">
      <polygon points="786,2240 890,2300 890,2420 786,2480 682,2420 682,2300" fill="url(#portraitFill)" stroke="var(--orange)" stroke-width="5"/>
    </g>
    <g role="img" aria-label="Portrait of a smiling client">
      <polygon points="1004,2236 1108,2296 1108,2416 1004,2476 900,2416 900,2296" fill="url(#portraitFill)"/>
    </g>
    <g role="img" aria-label="Portrait of a client in a suit">
      <polygon points="895,2427 999,2487 999,2607 895,2667 791,2607 791,2487" fill="url(#portraitFill)"/>
    </g>
  </svg>
</section>

<footer id="contact">
  <svg class="abs footer-bg" width="1200" height="401">
    <polygon points="0,107 600,0 1200,107 1200,401 0,401" fill="var(--footer)"/>
  </svg>
  <div class="abs footer-brand"><span class="brand-dot"></span>Orchid Digital</div>
  <p class="abs footer-small" style="top:2975px">Copyright © 2020, Company Name<br>All Right reserved</p>
  <p class="abs footer-small" style="top:3025px">Terms of Service, Privacy Policy</p>

  <div class="abs footer-col" style="left:381px;top:2877px">
    <h4>Quick Links</h4>
    <ul><li>Home</li><li>About Us</li><li>Services</li><li>How it Works</li><li>Testimonials</li><li>Contact Us</li></ul>
  </div>
  <div class="abs footer-col" style="left:604px;top:2877px">
    <h4>Case Studies</h4>
    <ul><li>Etiam hendrerit</li><li>Ante ut varius facilisis</li><li>Dolor lectus</li><li>Placerat massa</li><li>Dibendum</li></ul>
  </div>
  <div class="abs footer-col" style="left:864px;top:2877px"><h4>Contact Info</h4></div>

  <div class="abs contact-row" style="top:2908px">
    <svg width="10" height="14" viewBox="0 0 10 14" fill="#fff"><path d="M5 0a5 5 0 0 0-5 5c0 4 5 9 5 9s5-5 5-9a5 5 0 0 0-5-5zm0 7a2 2 0 1 1 0-4 2 2 0 0 1 0 4z"/></svg>
    <span>14 Linden Court, Street Name<br>Portland, USA</span>
  </div>
  <div class="abs contact-row" style="top:2959px">
    <svg width="12" height="12" viewBox="0 0 12 12" fill="#fff"><path d="M2.5 0 4.5 3 3.3 4.3a7 7 0 0 0 4.4 4.4L9 7.5l3 2-1.3 2C5 12 0 7 .5 1.3z"/></svg>
    <span>1-800-555-0142</span>
  </div>
  <div class="abs contact-row" style="top:2989px">
    <svg width="13" height="10" viewBox="0 0 13 10" fill="#fff"><path d="M0 0h13v1.5L6.5 6 0 1.5zM0 3l6.5 4.5L13 3v7H0z"/></svg>
    <span>hello@orchidmail.com</span>
  </div>
  <div class="abs social"><span>Chatterly</span><span>Pictly</span><span>Chirpa</span><span>Linkwork</span><span>Viewtube</span></div>
</footer>

</body>
</html>
```